Analytics/BI tech start-up seeks sharp, creative, simple, secret agent type logo & theme

"Quill 9 Dynamics" seeks a logo design/color scheme template for NYC based tech start-up of software engineers, solutions architects, and data/BI analysts. We develop reporting solutions and analytics platforms for small-medium sized businesses. We code for database, cloud, and web/mobile apps.<br/><br/>Some *very basic, limited* sketches are attached to show ideas we've had. We need a logo and color scheme that may be used for business cards, paper letterhead and envelopes, and web pages to be published at "www.quill9.dev".<br/><br/>We like the black/red, red/white, blue/black, white/black contrasts as a stating point, and prefer black background business cards, but open to anything if it feels like a good match. We are relying on the projects submitted here to take care of the creativity part of our image, which we work on logistics to launching our start-up. Something that could also be easily translated into black/white, grayscale would be appreciated as well. while log is important, we also need an icon that may be used as an app thumbnail. For font, we prefer all caps.<br/><br/>Business: Quill 9 Dynamics<br/>Slogan: If. Else. Us. / If -> Else -> Us / If - Else - Us / etc.<br/>Website: www.quill.dev<br/>Icon: [Q9] , only as a starting point<br/>Theme Ideas: Sleek, futuristic, secret agent-like tech, simple, bold color contrasts, software code related<br/><br/>Feel free to reach out to jdrevnik@mailvora.net as a contact for any questions or follow up. We look forward to seeing amazing ideas!
Updates

We would like to provide the opportunity for as many different submissions as possible.

Target Market(s)

Small business owners, entrepreneurs, financial/tech companies, freelance engineers, people in need of IT assistance to elevate business

Industry/Entity Type

It Company

Contact Information for Business Card

Individual Info: Name, Position, Phone Number 1, Phone Number 2 (optional), Fax Number, email Address.
Company Info: Name, logo, icon (optional), web site, slogan

Font styles to use
Sans Serif
Other font styles liked:
• Similar to Biome Light All Caps, Hollow Meridian type style

Requirements
Must have
• Pronounced 1 in the logo, either in the word Quill or not. Bold color contrast, one side with only logo or icon, possible web address too. Other side with all individual info plus logo, and/or icon and web address. If using uploaded files as a base, center the C more between the E and T, it is too closer to the T as is.
Nice to have
• Bolder font possibly, more square edged at ends of letters but still with minor curved corners. Icon suggested as a starting point is “[Q9]” and instead of a slogan, use "Data - Cloud - Web - Software" and the dividers don't necessary have to be hyphens.
Should not have
• Open to all creative ideas, try anything. Please come up with different logos than are in the attached files, they are meant as a starting point.

```html
<!DOCTYPE html>
<html lang="en">
<head>
<meta charset="utf-8">
<title>Quill 9 Dynamics — Business Card</title>
<link rel="stylesheet" href="https://fonts.googleapis.com/css2?family=Arimo:wght@400;700&family=Roboto+Condensed:wght@700&display=swap">
<style>
  :root {
    --bg: #1c1c1d;
    --card-dark: #2a2a2b;
    --logo-grey: #8c8c8e;
    --card-light: #ffffff;
    --ink: #111111;
    --ink-soft: #555555;
    --ink-muted: #8a8a8a;
    --rule: #9a9a9a;
  }
  * { box-sizing: border-box; margin: 0; padding: 0; }
  html, body { width: 1200px; height: 960px; overflow: hidden; }
  body {
    background: var(--bg);
    position: relative;
    font-family: "Arimo", Arial, sans-serif;
  }
  .card {
    position: absolute;
    left: 320px;
    width: 560px;
    height: 320px;
    box-shadow: 0 10px 30px rgba(0,0,0,.45);
  }
  .card--back {
    top: 110px;
    background: var(--card-dark);
    display: flex;
    align-items: center;
    justify-content: center;
  }
  .brand {
    display: flex;
    align-items: center;
    gap: 16px;
  }
  .brand__mark {
    width: 26px;
    height: 26px;
    background: var(--logo-grey);
    flex: none;
  }
  .brand__name {
    font-family: "Arimo", Arial, sans-serif;
    font-weight: 400;
    font-size: 40px;
    letter-spacing: 3px;
    color: var(--logo-grey);
    text-transform: uppercase;
    white-space: nowrap;
  }

  .card--front {
    top: 530px;
    background: var(--card-light);
    padding: 34px 40px;
  }
  .contact { width: 300px; font-size: 14px; color: var(--ink-soft); line-height: 1.3; }
  .contact__name {
    font-family: "Roboto Condensed", sans-serif;
    font-weight: 700;
    font-size: 20px;
    color: var(--ink);
    text-transform: uppercase;
    letter-spacing: .3px;
  }
  .contact__role { font-weight: 700; color: var(--ink-muted); font-size: 14px; }
  .contact__email { font-style: italic; }
  .divider {
    width: 110px;
    border: 0;
    border-top: 2px dotted var(--rule);
    margin: 14px 0;
  }
  .contact__label { font-weight: 700; }
  .contact__web { font-weight: 700; color: var(--ink-soft); }
  .services {
    position: absolute;
    right: 40px;
    top: 138px;
    font-family: "Roboto Condensed", sans-serif;
    font-weight: 700;
    font-size: 13px;
    color: var(--ink-soft);
    letter-spacing: .4px;
    text-transform: uppercase;
  }
</style>
</head>
<body>
  <section class="card card--back" aria-label="Card back">
    <div class="brand">
      <span class="brand__mark" aria-hidden="true"></span>
      <h1 class="brand__name">Quill 9 Dynamics</h1>
    </div>
  </section>

  <section class="card card--front" aria-label="Card front">
    <div class="contact">
      <p class="contact__name">Daniel Reyes</p>
      <p class="contact__role">President</p>
      <p class="contact__email">info@quill9dynamics.com</p>
      <hr class="divider">
      <p><span class="contact__label">Phone:</span> 555-204-7731</p>
      <p><span class="contact__label">Cell:</span> 555-318-6042</p>
      <p><span class="contact__label">Fax:</span> 555-427-1986</p>
      <hr class="divider">
      <p>4120 Larkspur Avenue</p>
      <p>Juneau, Alaska 99801</p>
      <p class="contact__web">quill9dynamics.com</p>
    </div>
    <p class="services">Data - Cloud - Web - Software</p>
  </section>
</body>
</html>
```